Manuka honey jar label for new Manuka brand

We are planning to start a Manuka honey brand and we need to design the label for the honey jar. Manuka honey is an up and coming product and the market is still young in our country.
Our market is dominated by 1 brand: Korivo Vital (photo attached). To the people who know what Manuka honey is, they associate it with Korivo Vital in the same way people associate Cola with Zibo Zesta or printer copies with Pluvex.
The good news is that a lot of people do not know yet what Manuka honey is and we still have the opportunity of being the first brand they get to know. At the same time, we still need to be able to take at least a bite out of the Korivo Vital market share.
The Korivo Vital label for their jar I think is not just absolutely gorgeous but it also does its job extremely well. It only features 3 informations:
- name of brand/logo (Korivo Vital)
- name of product (Manuka Honey)
- and mgo rating which is like a rating of how strong the honey is
By having just this information on a relatively small label, their label SCREAMS Manuka by having the Manuka words twice (the brand and the product name) and people develop this association between Korivo Vital and Manuka products in general.
Our product will also be in a similar square plastic jar. It will also be dark tinted, that´s important to note. We can also go for a blue cap but in order to differentiate ourselves from Korivo Vital we thought of maybe choosing a black lid instead. I uploaded 2 jars, 1 with black lid and 1 with gold (although it looks more like mustard) that you can use for simulations. They are pretty accurate of the type of jars and lids that we can have.
The label has total length of about 20cm. One side of the jar has 5,5 cm of the label and the height of the label is 4,5 cm. We can also use selective gold laminating on the label but we cannot have custom shape label at this point as Korivo Vital does with its tree logo that sticks outside the label.
I need the design for the entire label but the focus should be on the front part, that is the part that sells and catches your eye. Like Korivo Vital, the front part I want to have 3 vital informations:
- name of brand/logo (in our case Halvern Terra) - we do not have a pre-existing logo, this needs to be created alongside the label
- and mgo rating
As "other" information we also need the net weight "250 g" alongside with the typical "e" to appear on the front. That is a legal requirement.
Optionally, you can add a small phrase somewhere like "Harvested in New Zealand" or "Made in New Zealand" since this is a product that is only made there and in some areas of Australia.
This is pretty much all the info. As a final note, there are a ton of beautiful premium Manuka honey jar labels. But they are too fancy and when you look at them you don´t instantly recognize that it is Manuka Honey.
This instant recognition is vital! With this small jar there is the danger for customers to think that maybe it´s medicine, maybe it´s sports supplements etc. This is a relatively small product and imagine you just glance on it on the retail shelf. Instantly you must think it is Manuka Honey and that it is beautiful. And if you see it on the shelf next to Korivo Vital, it would be best to also think that you would rather buy this (it gives you more trust) than the Korivo Vital.
One final note: I do not want the bee as an insect on the label. I think some people are turned off when they see an insect with its small legs and make a bad association that there are insects inside. I do not mind symbolism or somehow super stylized bee in a modern way, but I do not want a plain insect on the label.
For any other questions, I am at your disposal. Thank you very much for taking the time to send us a proposal!

```html
<!DOCTYPE html>
<html lang="en">
<head>
<meta charset="utf-8">
<title>Halvern Terra Manuka Honey – Front Label</title>
<link href="https://fonts.googleapis.com/css2?family=Outfit:wght@400;500;600&display=swap" rel="stylesheet">
<style>
  :root {
    --page-bg: #eff0f2;
    --label-blue: #1d4488;
    --label-blue-light: #24509a;
    --gold: #e0a634;
    --gold-light: #f6e49a;
    --white: #ffffff;
    --paper: #f8f8f8;
    --ink: #2b2b2e;
  }
  * { margin: 0; padding: 0; box-sizing: border-box; }
  html, body {
    width: 1200px; height: 972px; overflow: hidden;
    background: var(--page-bg);
    font-family: "Outfit", sans-serif;
  }
  .label {
    position: absolute; left: 150px; top: 119px;
    width: 900px; height: 734px;
  }
  .label-top {
    position: absolute; left: 0; top: 0; width: 900px; height: 555px;
    background: linear-gradient(90deg, var(--label-blue-light), var(--label-blue) 40%, var(--label-blue));
  }
  .brand-name {
    position: absolute; left: 0; width: 900px; top: 22px;
    text-align: center; color: var(--gold);
    font-weight: 600; font-size: 52px; line-height: 64px;
  }
  .product-name {
    position: absolute; left: 0; width: 900px; top: 262px;
    text-align: center; color: var(--white);
    font-weight: 500; font-size: 102px; line-height: 120px; letter-spacing: -1px;
  }
  .rule {
    position: absolute; left: 91px; width: 715px; height: 3px; background: var(--white);
  }
  .rule-upper { top: 406px; }
  .rule-lower { top: 490px; }
  .origin {
    position: absolute; left: 0; width: 900px; top: 432px;
    text-align: center; color: var(--white);
    font-weight: 600; font-size: 29px; line-height: 34px; letter-spacing: 6px;
  }
  .gold-band {
    position: absolute; left: 0; top: 555px; width: 900px; height: 15px;
    background: linear-gradient(90deg, var(--gold), var(--gold-light) 55%, var(--gold));
  }
  .label-bottom {
    position: absolute; left: 0; top: 570px; width: 900px; height: 164px;
    background: var(--paper);
  }
  .mgo-badge { position: absolute; left: 79px; top: 29px; width: 191px; height: 107px; }
  .mgo-text {
    position: absolute; left: 79px; top: 29px; width: 191px; line-height: 107px;
    text-align: center; color: var(--white); font-weight: 500; font-size: 31px;
  }
  .mgo-text sup { font-size: 15px; }
  .net-weight {
    position: absolute; right: 88px; top: 62px;
    color: var(--ink); font-weight: 500; font-size: 38px; line-height: 42px;
  }
</style>
</head>
<body>
  <div class="label">
    <div class="label-top" role="img" aria-label="Navy blue background with a faint repeating flower tile pattern"></div>
    <div class="brand-name">Halvern<br>Terra</div>
    <div class="product-name">Manuka Honey</div>
    <div class="rule rule-upper"></div>
    <div class="origin">MADE IN NEW ZEALAND</div>
    <div class="rule rule-lower"></div>
    <div class="gold-band"></div>
    <div class="label-bottom">
      <svg class="mgo-badge" viewBox="0 0 191 107" aria-hidden="true">
        <polygon fill="var(--label-blue)" points="48,0 94,26.5 94,79.5 48,106 2,79.5 2,26.5"/>
        <polygon fill="var(--label-blue)" points="143,0 189,26.5 189,79.5 143,106 97,79.5 97,26.5"/>
        <rect fill="var(--label-blue)" x="80" y="26.5" width="30" height="53"/>
      </svg>
      <div class="mgo-text">MGO<sup>*</sup> 250</div>
      <div class="net-weight">℮ 250g</div>
    </div>
  </div>
</body>
</html>
```